I need a flyer designed for a marine service company. Our company specializes in boat engine diagnostic/repair, engine service, electronic installation and repairs, bottom paint, detailing, winterization and shrink wrapping. We would like to see designs that incorporate our color scheme of deep blue, blueish gray and black (please see attached photo)

Target Market(s)

Boat owners

Industry/Entity Type

Marine

Logo Text

Kelpridge Harbor Services

Requirements
Must have
• Company logo
Nice to have
• List the services we provide.

```html
<!DOCTYPE html>
<html lang="en">
<head>
<meta charset="utf-8">
<title>Kelpridge Harbor Services – Flyer</title>
<link rel="stylesheet" href="https://fonts.googleapis.com/css2?family=Playfair+Display:wght@400;700&family=Montserrat:wght@400;500;600;700&display=swap">
<style>
  :root {
    --deep-blue: #0f3a78;
    --ocean: #1d5fa6;
    --ocean-light: #3d86c6;
    --navy: #1b2a4a;
    --slate: #6f7f96;
    --ink: #1a1f2b;
    --paper: #ffffff;
    --star: #e0312f;
    --rule: #c9d2de;
  }
  * { box-sizing: border-box; margin: 0; padding: 0; }
  html, body { width: 769px; height: 1200px; overflow: hidden; background: var(--paper); }
  body { font-family: "Montserrat", sans-serif; color: var(--ink); }

  .flyer { position: relative; width: 769px; height: 1200px; background: var(--paper); }

  .hero {
    position: absolute; left: 0; top: 0; width: 769px; height: 665px;
    background: radial-gradient(ellipse at 78% 30%, var(--ocean-light) 0%, var(--ocean) 35%, var(--deep-blue) 75%, #0a2a5c 100%);
  }
  .brand { position: absolute; left: 52px; top: 92px; display: flex; align-items: center; gap: 12px; }
  .brand-dot { width: 22px; height: 22px; border-radius: 50%; background: var(--paper); }
  .brand-name { font-family: "Montserrat", sans-serif; font-weight: 600; font-size: 17px; letter-spacing: 2px; color: var(--paper); text-transform: uppercase; }

  .headline { position: absolute; left: 48px; top: 400px; color: var(--paper); }
  .headline h1 { font-family: "Playfair Display", serif; font-weight: 400; font-size: 74px; line-height: 0.98; letter-spacing: 1px; text-transform: uppercase; }
  .headline p { margin-top: 14px; font-family: "Montserrat", sans-serif; font-weight: 600; font-size: 30px; letter-spacing: 1.5px; text-transform: uppercase; }

  .services { position: absolute; left: 48px; top: 700px; width: 460px; }
  .services h2 { font-family: "Playfair Display", serif; font-weight: 400; font-size: 34px; color: var(--navy); padding-bottom: 8px; border-bottom: 2px solid var(--rule); width: 210px; }
  .service-grid { margin-top: 26px; display: grid; grid-template-columns: 1fr 1fr; row-gap: 26px; column-gap: 20px; }
  .service { display: flex; align-items: center; gap: 14px; font-size: 13px; font-weight: 500; line-height: 1.3; color: var(--ink); }
  .service svg { flex: 0 0 48px; }

  .gallery { position: absolute; right: 34px; top: 742px; width: 200px; display: flex; flex-direction: column; gap: 10px; }
  .gallery div { height: 84px; }
  .photo-engine { background: linear-gradient(135deg, #b7bfc9, #5c6775); }
  .photo-hull { background: linear-gradient(135deg, #d9dee4, #7d8896); }
  .photo-shop { background: linear-gradient(135deg, #8793a2, #3b4655); }

  .review { position: absolute; left: 48px; top: 1000px; width: 450px; display: flex; gap: 16px; }
  .avatar { flex: 0 0 70px; height: 70px; border-radius: 50%; background: linear-gradient(135deg, #8a6d55, #4e3b2e); }
  .stars { color: var(--star); font-size: 14px; letter-spacing: 2px; }
  .review p { font-size: 10px; line-height: 1.45; color: var(--slate); margin-top: 3px; }
  .review cite { display: block; font-style: normal; font-weight: 600; font-size: 10px; color: var(--ink); margin-top: 4px; }

  .contact { position: absolute; left: 0; top: 1110px; width: 769px; height: 70px; display: flex; align-items: center; justify-content: space-between; padding: 0 40px 0 48px; }
  .phone { display: flex; align-items: center; gap: 14px; font-weight: 700; font-size: 34px; color: var(--navy); }
  .email { display: flex; align-items: center; gap: 8px; font-size: 11px; color: var(--slate); }
  .email span.social { width: 16px; height: 16px; border-radius: 50%; background: var(--navy); display: inline-block; }
  .footer-band { position: absolute; left: 0; bottom: 0; width: 769px; height: 20px; background: var(--navy); }
</style>
</head>
<body>
<main class="flyer">
  <section class="hero" role="img" aria-label="Aerial photograph of a white motor boat cutting a wake across deep blue water">
    <div class="brand"><span class="brand-dot"></span><span class="brand-name">Kelpridge Harbor Services</span></div>
    <div class="headline">
      <h1>Kelpridge<br>Harbor</h1>
      <p>Marine Services</p>
    </div>
  </section>

  <section class="services">
    <h2>Our service</h2>
    <div class="service-grid">
      <div class="service">
        <svg width="48" height="48" viewBox="0 0 48 48"><circle cx="24" cy="24" r="22" fill="none" stroke="#1b2a4a" stroke-width="2"/><path d="M16 32 L28 20 M26 16 a5 5 0 1 0 6 6" fill="none" stroke="#1b2a4a" stroke-width="2.4" stroke-linecap="round"/></svg>
        <span>Boat engine<br>diagnostic/repair</span>
      </div>
      <div class="service">
        <svg width="48" height="48" viewBox="0 0 48 48"><circle cx="24" cy="24" r="22" fill="none" stroke="#1b2a4a" stroke-width="2"/><path d="M14 22 H34 L30 32 H18 Z M24 14 V22" fill="none" stroke="#1b2a4a" stroke-width="2.2" stroke-linejoin="round"/></svg>
        <span>Bottom paint</span>
      </div>
      <div class="service">
        <svg width="48" height="48" viewBox="0 0 48 48"><circle cx="24" cy="24" r="22" fill="none" stroke="#1b2a4a" stroke-width="2"/><circle cx="24" cy="24" r="6" fill="none" stroke="#1b2a4a" stroke-width="2.2"/><path d="M24 13 V16 M24 32 V35 M13 24 H16 M32 24 H35" stroke="#1b2a4a" stroke-width="2.4" stroke-linecap="round"/></svg>
        <span>Engine service</span>
      </div>
      <div class="service">
        <svg width="48" height="48" viewBox="0 0 48 48"><circle cx="24" cy="24" r="22" fill="none" stroke="#1b2a4a" stroke-width="2"/><path d="M24 14 l2.5 7 7 0 -5.5 4.5 2 7 -6-4 -6 4 2-7 -5.5-4.5 7 0 Z" fill="none" stroke="#1b2a4a" stroke-width="2" stroke-linejoin="round"/></svg>
        <span>Detailing</span>
      </div>
      <div class="service">
        <svg width="48" height="48" viewBox="0 0 48 48"><circle cx="24" cy="24" r="22" fill="none" stroke="#1b2a4a" stroke-width="2"/><path d="M26 12 L18 26 H24 L22 36 L30 22 H24 Z" fill="none" stroke="#1b2a4a" stroke-width="2.2" stroke-linejoin="round"/></svg>
        <span>Electronic<br>installation<br>and repairs</span>
      </div>
      <div class="service">
        <svg width="48" height="48" viewBox="0 0 48 48"><circle cx="24" cy="24" r="22" fill="none" stroke="#1b2a4a" stroke-width="2"/><path d="M24 13 V35 M15 18 L33 30 M33 18 L15 30" stroke="#1b2a4a" stroke-width="2.2" stroke-linecap="round"/></svg>
        <span>Winterization<br>and shrink<br>wrapping</span>
      </div>
    </div>
  </section>

  <aside class="gallery">
    <div class="photo-engine" role="img" aria-label="Photo of an outboard engine being serviced"></div>
    <div class="photo-hull" role="img" aria-label="Photo of a boat hull on stands in the yard"></div>
    <div class="photo-shop" role="img" aria-label="Photo of technicians working on a boat in the shop"></div>
  </aside>

  <section class="review">
    <div class="avatar" role="img" aria-label="Portrait photo of a satisfied customer"></div>
    <div>
      <div class="stars">★★★★★</div>
      <p>Kelpridge Harbor Services kept our cruiser running all season. Fast diagnosis, fair pricing and careful work on every detail. Highly recommended for any boat owner on the bay.</p>
      <cite>Marina Hollis</cite>
    </div>
  </section>

  <footer class="contact">
    <div class="phone">
      <svg width="30" height="30" viewBox="0 0 24 24"><path d="M6.6 10.8a15 15 0 0 0 6.6 6.6l2.2-2.2a1 1 0 0 1 1-.25 11.4 11.4 0 0 0 3.6.57 1 1 0 0 1 1 1V20a1 1 0 0 1-1 1A17 17 0 0 1 3 4a1 1 0 0 1 1-1h3.5a1 1 0 0 1 1 1c0 1.25.2 2.45.57 3.6a1 1 0 0 1-.25 1Z" fill="#1b2a4a"/></svg>
      <span>1 555-014-2290</span>
    </div>
    <div class="email">
      <span>hello@kelpridgeharbor.com</span>
      <span class="social"></span>
    </div>
  </footer>
  <div class="footer-band"></div>
</main>
</body>
</html>
```